Flyer Design Project

Something bold, something creative, something colorful. Will have 3 full time employees passing these out to business owners locally as well as national conventions.
Need something that will grab attention and remain a reminder, before they end up hitting the trash can...
Site can be found at www.KelvoraPress.example
A few different logo formats are attached.
2 sizes would be nice. 8.5" x 11" and 4"x6 (they can look the same)
No specifics on graphics, colors or info. Stay somewhat consistent with the website. I basically just want people to know we are here and we are definitely the cheapest print prices in the nation.
Target Market(s)
Anyone that needs print work done.
Industry/Entity Type
Business
Look and feel
Each slider illustrates characteristics of the customer's brand and the style your logo design should communicate.

```html
<!DOCTYPE html>
<html lang="en">
<head>
<meta charset="utf-8">
<title>Kelvora Press — Nobody Beats Our Print Prices</title>
<link rel="stylesheet" href="https://fonts.googleapis.com/css2?family=Bebas+Neue&family=Montserrat:wght@500&display=swap">
<style>
  :root {
    --paper: #ffffff;
    --orange: #f26849;
    --magenta: #c0579a;
    --green: #9cc45e;
    --teal: #52be9e;
    --yellow: #ffcb4f;
    --ink: #2b2b2b;
  }
  html, body {
    margin: 0;
    padding: 0;
    overflow: hidden;
    background: var(--paper);
  }
  .flyer {
    position: relative;
    width: 923px;
    height: 1200px;
    background: var(--paper);
    overflow: hidden;
    font-family: "Bebas Neue", "Arial Narrow", sans-serif;
  }
  .headline {
    margin: 0;
    font-weight: 400;
  }
  .headline__line {
    position: absolute;
    left: 0;
    width: 100%;
    text-align: center;
    line-height: 0.72;
    white-space: nowrap;
  }
  .headline__line--nobody  { top: 228px; font-size: 186px; color: var(--orange);  letter-spacing: 3px; }
  .headline__line--beats   { top: 372px; font-size: 240px; color: var(--magenta); letter-spacing: 4px; }
  .headline__line--print   { top: 578px; font-size: 119px; color: var(--green);   letter-spacing: 1px; }
  .headline__line--prices  { top: 684px; font-size: 196px; color: var(--teal);    letter-spacing: 3px; }
  .guarantee {
    position: absolute;
    top: 852px;
    left: 0;
    width: 100%;
    margin: 0;
    text-align: center;
    font-size: 83px;
    line-height: 0.72;
    color: var(--yellow);
    white-space: nowrap;
  }
  .brand {
    position: absolute;
    top: 1040px;
    left: 0;
    width: 100%;
    display: flex;
    justify-content: center;
    align-items: center;
    gap: 22px;
  }
  .brand__mark {
    width: 80px;
    height: 80px;
    flex: none;
  }
  .brand__text {
    display: flex;
    flex-direction: column;
    align-items: flex-end;
  }
  .brand__name {
    font-family: "Bebas Neue", "Arial Narrow", sans-serif;
    font-size: 72px;
    line-height: 0.8;
    color: var(--ink);
    letter-spacing: 1px;
  }
  .brand__tagline {
    margin-top: 6px;
    font-family: "Montserrat", Arial, sans-serif;
    font-weight: 500;
    font-size: 18px;
    color: var(--ink);
  }
</style>
</head>
<body>
  <main class="flyer">
    <h1 class="headline">
      <span class="headline__line headline__line--nobody">Nobody</span>
      <span class="headline__line headline__line--beats">Beats</span>
      <span class="headline__line headline__line--print">Our Print</span>
      <span class="headline__line headline__line--prices">Prices!</span>
    </h1>
    <p class="guarantee">100% Guaranteed</p>

    <footer class="brand">
      <svg class="brand__mark" viewBox="0 0 80 80" aria-hidden="true">
        <circle cx="40" cy="40" r="34" fill="var(--magenta)"/>
      </svg>
      <div class="brand__text">
        <span class="brand__name">Kelvora Press</span>
        <span class="brand__tagline">Discount Print and Promo</span>
      </div>
    </footer>
  </main>
</body>
</html>
```